Poster Design Project for an Old-fashioned Ice Cream Parlor

We are an old-fashioned American ice cream company called Bemick's Ice Cream based in the San Francisco Bay Area. We would like a poster design to be put up on display in our parlors. The design should embody the American 1950s retro/vintage look that our company already identifies with, but spruced up with a modern touch. Feel free to be as creative as you like and remix it with your own style! There will be 3 winners and we are hoping for a variety of styles. Each winner will be rewarded with $130. We look forward to seeing your work!
Updates

Hello all,

In reply to some comments, I have uploaded our logo under the 'brief'. Our company was established in 1950. 

Industry/Entity Type

It Company

Requirements
Must have
• the 3 final posters we will select must be formatted to 18x22 inches
designs that incorporate pink, blue, and yellow (our brand colors) will be more likely to win; these colors do not have to be a major part of the artwork
Nice to have
• include the colors pink, blue, and yellow
Should not have
• designs should not be dark in theme

```html
<!DOCTYPE html>
<html lang="en">
<head>
<meta charset="utf-8">
<title>Bemick's Ice Cream — Since 1950</title>
<link rel="stylesheet" href="https://fonts.googleapis.com/css2?family=Jost:wght@500;600;700&display=swap">
<style>
  :root {
    --bg-lime: #e2e8a1;
    --type-white: #ffffff;
    --brand-navy: #2f5ea6;
    --scoop-pink: #f28bb4;
    --scoop-pink-light: #f9d3e1;
    --cone-pink: #ee6f9e;
    --scoop-blue: #86c6e6;
    --scoop-blue-light: #cfe8f3;
    --cone-blue: #7fbfe3;
    --scoop-yellow: #f7e21b;
    --scoop-amber: #e8a21c;
    --cone-orange: #f2a516;
  }
  * { margin: 0; padding: 0; box-sizing: border-box; }
  html, body {
    width: 982px;
    height: 1200px;
    overflow: hidden;
    background: var(--bg-lime);
  }
  .poster {
    position: relative;
    width: 982px;
    height: 1200px;
    background: var(--bg-lime);
    font-family: "Jost", "Futura", sans-serif;
    color: var(--type-white);
    overflow: hidden;
  }
  .headline {
    position: absolute;
    left: 0;
    width: 100%;
    text-align: center;
    line-height: 1;
    font-weight: 500;
  }
  .headline--since {
    top: 22px;
    font-size: 302px;
    letter-spacing: -4px;
  }
  .headline--year {
    top: 284px;
    font-size: 378px;
    letter-spacing: -10px;
  }
  .tagline {
    position: absolute;
    top: 612px;
    left: 0;
    width: 100%;
    text-align: center;
    font-size: 56px;
    font-weight: 600;
    line-height: 1;
    letter-spacing: 0.5px;
  }
  .cone-photo {
    position: absolute;
    top: 712px;
    height: 488px;
    border-radius: 130px 130px 0 0;
  }
  .cone-photo--pink {
    left: 62px;
    width: 284px;
    background: linear-gradient(180deg, var(--scoop-pink) 0%, var(--scoop-pink-light) 30%, var(--cone-pink) 60%, var(--bg-lime) 100%);
  }
  .cone-photo--blue {
    left: 349px;
    width: 282px;
    background: linear-gradient(180deg, var(--scoop-blue) 0%, var(--scoop-blue-light) 30%, var(--cone-blue) 60%, var(--bg-lime) 100%);
  }
  .cone-photo--yellow {
    left: 637px;
    width: 284px;
    background: linear-gradient(180deg, var(--scoop-amber) 0%, var(--scoop-yellow) 30%, var(--cone-orange) 60%, var(--bg-lime) 100%);
  }
  .brand-mark {
    position: absolute;
    top: 1004px;
    left: 0;
    width: 100%;
    display: flex;
    justify-content: center;
    align-items: center;
    gap: 10px;
  }
  .brand-mark__dot {
    width: 18px;
    height: 18px;
    border-radius: 50%;
    background: var(--brand-navy);
  }
  .brand-mark__name {
    font-size: 34px;
    font-weight: 700;
    color: var(--brand-navy);
    line-height: 1;
  }
</style>
</head>
<body>
  <main class="poster">
    <h1 class="headline headline--since">SINCE</h1>
    <p class="headline headline--year">1950</p>
    <p class="tagline">HOW ICE CREAM USED TO BE</p>

    <div class="cone-photo cone-photo--pink" role="img" aria-label="Photo of a pink waffle cone with three scoops of pink ice cream"></div>
    <div class="cone-photo cone-photo--blue" role="img" aria-label="Photo of a blue waffle cone with three scoops of blue ice cream"></div>
    <div class="cone-photo cone-photo--yellow" role="img" aria-label="Photo of an orange waffle cone with three scoops of yellow ice cream"></div>

    <div class="brand-mark">
      <span class="brand-mark__dot"></span>
      <span class="brand-mark__name">Bemick's</span>
    </div>
  </main>
</body>
</html>
```